依頼詳細
現状、施工した場所に施工済ステッカーを貼っているのですが、
今回施工をしたホテル様の要望で、フロントや客室にお客様へ向けたアピールできるチラシなどが欲しいといわれました。
ホテルのフロント・客室の卓上におけるものや・車内に貼れるものなので
年賀状サイズくらいで検討しています。

イメージは
・主成分でもある青森ヒバをモチーフにしたもの
・一目でわかる安心感が伝わるもの
・100%天然成分で安心安全
・キャッチコピーは『植物の力で抗菌中!』

記載項目
ヴェルトナ産業株式会社 0120-387-905
Lumiva Plus
サイズ
年賀状サイズくらい
ページ数
片面
希望イメージ
シンプル 複雑
単色 カラフル
暗い 明るい
日常 高級
遊び心 厳粛
未来的 伝統的
女性的 男性的
希望する色
緑系、青系
納品ファイル
• 高解像度JPG (.jpg)
補足説明
当社が使用しているチラシです。
■ 選んだ理由

どの候補者もとても良かったですが、
こちらはどのシチュエーションでもあうようなデザインかつ
柔らかい印象で、安心感を与えてくれるようなデザインなので決めました。

■ 提案者全員のお礼・コメント

とても素晴らしいデザインばかりでかなり迷いました。
予算があれば他の候補者も当選sて他のですが。
今後は社のチラシなども作成予定ですので、
またお願いするかと思います。
宜しくお願い致します。

```html
<!DOCTYPE html>
<html lang="ja">
<head>
<meta charset="utf-8">
<title>植物の力で抗菌中！</title>
<link rel="stylesheet" href="https://fonts.googleapis.com/css2?family=Noto+Sans+JP:wght@700;900&family=Noto+Serif+JP:wght@700;900&display=swap">
<style>
  :root {
    --sky-deep: #0a2a8c;
    --sky-mid: #1f5fd0;
    --sky-glow: #8fd0ff;
    --forest: #1d3550;
    --shield-green: #1f9a4a;
    --shield-green-light: #4cc46a;
    --shield-rim: #e9f1f4;
    --shield-rim-shade: #9fb2bd;
    --ink-green: #0e5a2a;
    --alert-red: #e0202a;
    --white: #ffffff;
  }
  * { margin: 0; padding: 0; box-sizing: border-box; }
  html, body { width: 811px; height: 1200px; overflow: hidden; background: var(--sky-deep); }
  .flyer {
    position: relative;
    width: 811px;
    height: 1200px;
    overflow: hidden;
    font-family: "Noto Serif JP", serif;
    color: var(--white);
  }
  .backdrop {
    position: absolute;
    inset: 0;
    background:
      radial-gradient(ellipse 60% 40% at 50% 55%, rgba(143,208,255,0.75), rgba(143,208,255,0) 70%),
      linear-gradient(180deg, var(--sky-deep) 0%, var(--sky-mid) 40%, #3f86dc 60%, #2a4f80 80%, var(--forest) 100%);
  }
  .headline {
    position: absolute;
    top: 58px;
    left: 0;
    width: 100%;
    text-align: center;
    font-weight: 900;
    font-size: 46px;
    line-height: 1.3;
    text-shadow: 0 2px 6px rgba(0,0,30,0.5);
  }
  .shield {
    position: absolute;
    left: 140px;
    top: 222px;
    width: 531px;
    height: 680px;
  }
  .catch {
    position: absolute;
    left: 0;
    width: 100%;
    text-align: center;
    font-family: "Noto Sans JP", sans-serif;
    font-weight: 900;
    paint-order: stroke fill;
    -webkit-text-stroke: 10px var(--white);
    letter-spacing: 0.01em;
    filter: drop-shadow(0 4px 4px rgba(0,40,10,0.45));
  }
  .catch--plant { top: 378px; font-size: 88px; color: var(--ink-green); }
  .catch--anti { top: 505px; font-size: 104px; color: var(--alert-red); }
  .leaf-mark {
    position: absolute;
    left: 348px;
    top: 665px;
    width: 115px;
    height: 85px;
    border-radius: 50%;
    background: radial-gradient(ellipse at 40% 40%, #c8f0a8, #4bb84e 60%, #2c8a37);
    opacity: 0.95;
  }
  .company {
    position: absolute;
    top: 905px;
    left: 0;
    width: 100%;
    text-align: center;
    font-family: "Noto Sans JP", sans-serif;
    font-weight: 900;
    font-size: 38px;
    text-shadow: 0 2px 5px rgba(0,0,20,0.6);
  }
  .phone {
    position: absolute;
    top: 985px;
    left: 0;
    width: 100%;
    display: flex;
    justify-content: center;
    align-items: center;
    gap: 10px;
    font-weight: 900;
    font-size: 86px;
    line-height: 1;
    text-shadow: 0 3px 6px rgba(0,0,20,0.6);
  }
  .phone-icon { width: 72px; height: 60px; }
  .product {
    position: absolute;
    right: 52px;
    bottom: 34px;
    font-weight: 700;
    font-size: 28px;
    text-shadow: 0 2px 4px rgba(0,0,20,0.6);
  }
</style>
</head>
<body>
<main class="flyer">
  <div class="backdrop" role="img" aria-label="見上げた青森ヒバの森と青空、漂うウイルスの背景写真"></div>

  <p class="headline">100%天然成分で<br>安心安全</p>

  <svg class="shield" viewBox="0 0 531 680" aria-hidden="true">
    <defs>
      <linearGradient id="rim" x1="0" y1="0" x2="1" y2="1">
        <stop offset="0" stop-color="var(--shield-rim)"/>
        <stop offset="0.5" stop-color="var(--shield-rim-shade)"/>
        <stop offset="1" stop-color="var(--shield-rim)"/>
      </linearGradient>
      <linearGradient id="face" x1="0" y1="0" x2="0" y2="1">
        <stop offset="0" stop-color="var(--shield-green-light)"/>
        <stop offset="1" stop-color="var(--shield-green)"/>
      </linearGradient>
    </defs>
    <path d="M10 20 Q140 60 265 8 Q391 60 521 20 L521 330 Q510 520 265 672 Q21 520 10 330 Z" fill="url(#rim)"/>
    <path d="M34 46 Q150 80 265 36 Q381 80 497 46 L497 330 Q488 505 265 640 Q42 505 34 330 Z" fill="url(#face)"/>
    <path d="M34 46 Q150 80 265 36 Q381 80 497 46 L497 200 Q265 240 34 200 Z" fill="#ffffff" opacity="0.12"/>
  </svg>

  <p class="catch catch--plant">植物の力で</p>
  <p class="catch catch--anti">抗菌中!</p>
  <div class="leaf-mark" role="img" aria-label="二枚の葉のイラスト"></div>

  <p class="company">ヴェルトナ産業株式会社</p>
  <p class="phone">
    <svg class="phone-icon" viewBox="0 0 72 60" aria-hidden="true">
      <path d="M4 22 Q36 0 68 22 L62 32 L50 26 L50 18 Q36 12 22 18 L22 26 L10 32 Z" fill="var(--white)"/>
      <path d="M18 30 L54 30 L64 56 L8 56 Z" fill="var(--white)"/>
      <circle cx="36" cy="43" r="8" fill="var(--sky-mid)"/>
    </svg>
    <span class="phone-number">0120-387-905</span>
  </p>
  <p class="product">Lumiva Plus</p>
</main>
</body>
</html>
```